Theatre company seeking web designer/programmer

We are a theatre company re-branding and looking for a web programmer to build the site we have designed. We are an outside the box theatre company and have designed an a-typical website for ourselves. We need a programmer comfortable with HTML5 to build the site and its limited but important animation.

There should be about 5 pages themselves- most incredibly simple and we essentially have them designed already. We need someone who can build what we have designed, and program the small amount of animation we have.

I have a video attached to this project showing the landing page and home page. The animation on the landing page is the most complicated the site gets. I have the other pages designed as well and can send along to the person selected for this project.

We also hope to keep a working, project-by-project relationship with our designer/programmer, as updates for the site come up (For additional project-by project funding.)

Industry/Entity Type

It Company

Coding

Coded - Design and coding required

Number of Pages Required

5+ page

Colors
ec1f27
ffcf3e
0255a3
000000
ffffff

Requirements
Must have
• The ability to program our animation.
Nice to have
• A desire to work with us again in the future as we need updates to the site.

```html
<!DOCTYPE html>
<html lang="en">
<head>
<meta charset="utf-8">
<title>The Outlier Guild — The Summer I Disappeared</title>
<link rel="stylesheet" href="https://fonts.googleapis.com/css2?family=Chelsea+Market&family=Open+Sans:wght@400&display=swap">
<style>
  :root {
    --ink-black: #000000;
    --night: #1a1a1a;
    --smoke: #2b2b2b;
    --paper-white: #ffffff;
    --signal-red: #ec1f27;
  }
  * { box-sizing: border-box; margin: 0; padding: 0; }
  html, body {
    width: 1200px;
    height: 669px;
    overflow: hidden;
    background: var(--ink-black);
  }
  .stage {
    position: relative;
    width: 1200px;
    height: 669px;
    overflow: hidden;
    color: var(--paper-white);
    font-family: "Chelsea Market", fantasy;
  }
  .stage-backdrop {
    position: absolute;
    inset: 0;
    background:
      radial-gradient(ellipse at 35% 30%, rgba(90,90,90,0.35), transparent 45%),
      radial-gradient(ellipse at 70% 60%, rgba(70,70,70,0.3), transparent 50%),
      linear-gradient(160deg, var(--smoke) 0%, var(--night) 55%, #111111 100%);
  }
  .brand-name {
    position: absolute;
    left: 0; right: 0;
    top: 76px;
    text-align: center;
    font-size: 40px;
    letter-spacing: 1px;
    text-transform: uppercase;
  }
  .main-nav a {
    position: absolute;
    top: 168px;
    color: var(--paper-white);
    text-decoration: none;
    font-size: 24px;
    text-transform: uppercase;
    transform: translateX(-50%);
    white-space: nowrap;
  }
  .main-nav .nav-about { left: 279px; }
  .main-nav .nav-members { left: 917px; }
  .event {
    position: absolute;
    left: 0; right: 0;
    top: 276px;
    text-align: center;
    text-transform: uppercase;
  }
  .event-date { font-size: 22px; line-height: 28px; }
  .event-title { font-size: 46px; line-height: 56px; margin-top: 26px; font-weight: 400; }
  .event-host { font-size: 18px; line-height: 24px; margin-top: 20px; }
  .join-button {
    position: absolute;
    left: 505px;
    top: 460px;
    width: 190px;
    height: 48px;
    border-radius: 24px;
    background: var(--signal-red);
    color: var(--paper-white);
    text-decoration: none;
    text-transform: uppercase;
    font-size: 22px;
    display: flex;
    align-items: center;
    justify-content: center;
  }
  .site-footer {
    position: absolute;
    left: 86px;
    top: 628px;
    font-family: "Open Sans", sans-serif;
    font-size: 13px;
  }
</style>
</head>
<body>
  <main class="stage">
    <div class="stage-backdrop" role="img" aria-label="Dark moody photograph of a night scene with a full moon, in black and grey tones"></div>

    <header>
      <div class="brand-name">The Outlier Guild</div>
      <nav class="main-nav">
        <a class="nav-about" href="#about">About Members</a>
        <a class="nav-members" href="#members">Members Only</a>
      </nav>
    </header>

    <section class="event">
      <p class="event-date">May 1961</p>
      <h1 class="event-title">The Summer I Disappeared</h1>
      <p class="event-host">A Beat Poetry Salon hosted by Mara Lindqvist &amp; TOG</p>
    </section>

    <a class="join-button" href="#join">Join Us</a>

    <footer class="site-footer">© 2015 Copy Rights.The Outlier Guild.All Rights Reserved.</footer>
  </main>
</body>
</html>
```